Business card design for engineering firm specializing in defense industry.

We need a professional business card design. Something simple but stands out. We are an engineering company specializing in composites in the defense industry.
Industry/Entity Type
Defense
Contact Information for Business Card
A simple black business card with the Fibrolane yellow color is what we had in mind but open for other designs.
Colors
ffc214

```html
<!DOCTYPE html>
<html lang="en">
<head>
<meta charset="utf-8">
<title>Fibrolane Business Card</title>
<link href="https://fonts.googleapis.com/css2?family=Exo+2:wght@700&family=Lato:wght@400&display=swap" rel="stylesheet">
<style>
  :root {
    --page: #2b2b2b;
    --card: #1d1d1f;
    --brand-yellow: #ffc214;
    --ink: #ffffff;
    --muted-logo: #3a3a3c;
    --rule: #d9d9d9;
  }
  * { margin: 0; padding: 0; box-sizing: border-box; }
  html, body {
    width: 1200px; height: 895px; overflow: hidden;
    background: var(--page);
    font-family: "Lato", sans-serif;
  }
  .stage { position: relative; width: 1200px; height: 895px; }
  .card {
    position: absolute;
    width: 600px; height: 343px;
    background: var(--card);
    overflow: hidden;
    box-shadow: 0 14px 30px rgba(0,0,0,.45);
  }
  .card--front { left: 130px; top: 70px; }
  .card--back { left: 470px; top: 480px; }
  .corner-accents { position: absolute; inset: 0; }

  .wordmark {
    font-family: "Exo 2", sans-serif;
    font-weight: 700;
    letter-spacing: 0.5px;
    display: flex; align-items: center; gap: 12px;
  }
  .wordmark__square { width: 18px; height: 18px; background: var(--brand-yellow); }
  .card--front .wordmark {
    position: absolute; left: 0; right: 0; top: 138px;
    justify-content: center;
    font-size: 54px; color: var(--muted-logo);
  }
  .card--front .wordmark__square { background: var(--muted-logo); }
  .card--back .wordmark {
    position: absolute; left: 40px; top: 150px;
    font-size: 44px; color: var(--ink);
  }

  .divider {
    position: absolute; left: 318px; top: 70px;
    width: 1px; height: 210px; background: var(--rule);
  }
  .contact { position: absolute; left: 340px; top: 62px; color: var(--ink); }
  .contact__name {
    font-family: "Exo 2", sans-serif; font-weight: 700;
    font-size: 22px; color: var(--brand-yellow); line-height: 1;
  }
  .contact__role { font-size: 12px; margin-top: 4px; }
  .contact__address { font-size: 12px; line-height: 1.45; margin-top: 20px; margin-left: 14px; }
  .contact__list { list-style: none; margin-top: 18px; margin-left: 14px; font-size: 12px; }
  .contact__list li { display: flex; align-items: center; gap: 9px; line-height: 1.55; }
  .contact__list svg { width: 11px; height: 11px; flex: none; fill: var(--brand-yellow); }
</style>
</head>
<body>
<main class="stage">

  <section class="card card--front" aria-label="Card front">
    <svg class="corner-accents" viewBox="0 0 600 343" aria-hidden="true">
      <polygon points="0,0 70,0 0,45" fill="var(--brand-yellow)"/>
      <polygon points="530,0 600,0 600,40" fill="var(--brand-yellow)"/>
      <polygon points="0,280 0,343 55,343" fill="var(--brand-yellow)"/>
      <polygon points="600,300 600,343 540,343" fill="var(--brand-yellow)"/>
    </svg>
    <div class="wordmark"><span class="wordmark__square"></span>Fibrolane</div>
  </section>

  <section class="card card--back" aria-label="Card back">
    <div class="wordmark"><span class="wordmark__square"></span>Fibrolane</div>
    <div class="divider"></div>
    <div class="contact">
      <p class="contact__name">Marcus Halden</p>
      <p class="contact__role">Founder</p>
      <p class="contact__address">4820 N. Harlow Avenue, Suite 140<br>Lincoln, NE 68510</p>
      <ul class="contact__list">
        <li><svg viewBox="0 0 12 12"><path d="M3 0h6v12H3zM4 1.5v8h4v-8z"/></svg>(000) 000-0000</li>
        <li><svg viewBox="0 0 12 12"><path d="M2 1l3 0 1 3-2 1a7 7 0 0 0 3 3l1-2 3 1v3l-1 1C5 11 1 7 1 2z"/></svg>(999) 999-9999</li>
        <li><svg viewBox="0 0 12 12"><path d="M3 0h6v3H3zM0 4h12v5H10v3H2V9H0zM3 8v3h6V8z"/></svg>(666) 666-6666</li>
        <li><svg viewBox="0 0 12 12"><path d="M0 2h12v8H0zM1 3l5 4 5-4z" fill-rule="evenodd"/></svg>halden@fibrolane.com</li>
        <li><svg viewBox="0 0 12 12"><circle cx="6" cy="6" r="5.5" fill="none" stroke="var(--brand-yellow)"/><path d="M0.5 6h11M6 .5v11" stroke="var(--brand-yellow)" fill="none"/><ellipse cx="6" cy="6" rx="2.5" ry="5.5" fill="none" stroke="var(--brand-yellow)"/></svg>www.fibrolane.com</li>
      </ul>
    </div>
  </section>

</main>
</body>
</html>
```